Doctors clinic requires stationary designed

We require various types of stationary to be design based on the logo (attached). We require the following:
- Letterhead (A4 Portrait)
- Business Card (must include UV spot on rear)
- With compliments slip (DL Landscape)
- Appointments card (Folded A6)

We are a young clinical practice which boasts a modern and sophisticated approach to medicine so we require something which feels fresh and modern. Please include colours represented in the logo (contrasting teal and grey). We are calling for creative minds to put forth their ideas and we will be actively providing feedback on all designs.

thank you

Clinic

```html
<!DOCTYPE html>
<html lang="en">
<head>
<meta charset="utf-8">
<title>Dr Clara Whitfield – Stationery Suite</title>
<link href="https://fonts.googleapis.com/css2?family=Ubuntu:wght@400;500&family=Roboto:wght@400;700&display=swap" rel="stylesheet">
<style>
  :root {
    --teal: #1a958f;
    --mint: #73c19e;
    --green-text: #2c9a80;
    --grey-bar: #a5a5a5;
    --rule: #8f8f8f;
    --paper: #ffffff;
    --backdrop: #ecebe7;
    --shadow: 0 3px 8px rgba(0,0,0,.22);
  }
  * { box-sizing: border-box; margin: 0; padding: 0; }
  html, body { width: 1200px; height: 1120px; overflow: hidden; }
  body { background: var(--backdrop); position: relative; font-family: "Ubuntu", sans-serif; }

  .piece { position: absolute; background: var(--paper); box-shadow: var(--shadow); }
  .sheet-mint { position: absolute; background: var(--mint); box-shadow: var(--shadow); }
  .sheet-teal { position: absolute; background: var(--teal); box-shadow: var(--shadow); }

  .brand { display: flex; align-items: center; gap: 8px; color: var(--teal); }
  .brand-dot { border: 2px solid var(--teal); border-radius: 50%; flex: none; }
  .brand-name { font-weight: 500; line-height: 1; }
  .brand-role { font-weight: 500; line-height: 1; margin-top: 3px; }

  .mark { position: absolute; border: 2px solid var(--teal); border-radius: 50%; }

  .row { display: flex; gap: 3px; }
  .row span { display: block; height: 100%; }
  .hd span { background: var(--mint); }
  .tx span { background: var(--grey-bar); }
  .mix .m { background: var(--mint); }
  .mix .g { background: var(--grey-bar); }

  .rule { position: absolute; height: 1px; background: var(--rule); }

  .card-title { position: absolute; font-family: "Roboto", sans-serif; font-weight: 700; color: var(--green-text); font-size: 11px; }
  .sign-label { position: absolute; font-family: "Roboto", sans-serif; font-size: 7px; color: #444; }
  .signature { position: absolute; background: linear-gradient(90deg, rgba(60,60,60,.25), rgba(60,60,60,.08)); border-radius: 8px; }

  .flap { position: absolute; left: 0; top: 0; }
  .back-text { position: absolute; font-family: "Roboto", sans-serif; color: var(--green-text); line-height: 1.25; }
</style>
</head>
<body>

<!-- Letterhead -->
<div class="sheet-mint" style="left:564px;top:128px;width:389px;height:537px;"></div>
<div class="sheet-teal" style="left:682px;top:160px;width:388px;height:538px;"></div>
<section class="piece letterhead" style="left:661px;top:118px;width:371px;height:526px;">
  <div class="brand" style="position:absolute;left:48px;top:42px;">
    <span class="brand-dot" style="width:50px;height:50px;"></span>
    <div>
      <div class="brand-name" style="font-size:16px;">Dr Clara Whitfield</div>
      <div class="brand-role" style="font-size:9px;">Obstetrician and Gynaecologist</div>
    </div>
  </div>

  <div class="row hd" style="position:absolute;left:48px;top:157px;height:5px;">
    <span style="width:18px"></span><span style="width:5px"></span><span style="width:20px"></span><span style="width:6px"></span><span style="width:32px"></span><span style="width:12px"></span><span style="width:30px"></span><span style="width:18px"></span>
  </div>
  <svg style="position:absolute;left:48px;top:172px;" width="270" height="70">
    <g fill="#a5a5a5">
      <rect y="0" width="260" height="3"/><rect y="6" width="255" height="3"/><rect y="12" width="262" height="3"/><rect y="18" width="258" height="3"/><rect y="24" width="262" height="3"/><rect y="30" width="110" height="3"/>
      <rect y="44" width="258" height="3"/><rect y="50" width="266" height="3"/><rect y="56" width="80" height="3"/>
    </g>
  </svg>

  <div class="row hd" style="position:absolute;left:48px;top:248px;height:5px;">
    <span style="width:18px"></span><span style="width:5px"></span><span style="width:20px"></span><span style="width:6px"></span><span style="width:32px"></span><span style="width:12px"></span><span style="width:30px"></span><span style="width:18px"></span><span style="width:26px"></span>
  </div>
  <svg style="position:absolute;left:48px;top:262px;" width="270" height="70">
    <g fill="#a5a5a5">
      <rect y="0" width="260" height="3"/><rect y="6" width="255" height="3"/><rect y="12" width="262" height="3"/><rect y="18" width="258" height="3"/><rect y="24" width="262" height="3"/><rect y="30" width="110" height="3"/>
      <rect y="36" width="258" height="3"/><rect y="42" width="266" height="3"/><rect y="48" width="80" height="3"/><rect y="54" width="262" height="3"/><rect y="60" width="262" height="3"/>
    </g>
  </svg>

  <div class="sign-label" style="left:198px;top:354px;">Lorem ipsum</div>
  <div class="signature" role="img" aria-label="Handwritten signature" style="left:252px;top:348px;width:66px;height:20px;"></div>

  <svg style="position:absolute;left:118px;top:458px;" width="140" height="20">
    <g fill="#73c19e"><rect x="0" y="0" width="16" height="3"/><rect x="0" y="6" width="14" height="3"/><rect x="16" y="6" width="16" height="3"/><rect x="60" y="6" width="18" height="3"/><rect x="82" y="6" width="20" height="3"/><rect x="55" y="12" width="20" height="3"/></g>
    <g fill="#a5a5a5"><rect x="18" y="0" width="30" height="3"/><rect x="50" y="0" width="38" height="3"/><rect x="36" y="6" width="20" height="3"/><rect x="105" y="6" width="18" height="3"/><rect x="10" y="12" width="40" height="3"/><rect x="78" y="12" width="42" height="3"/></g>
  </svg>
</section>

<!-- Appointment card (folded, open flat) -->
<section class="piece appt-inner" style="left:130px;top:259px;width:139px;height:294px;">
  <div class="brand" style="position:absolute;left:26px;top:14px;gap:4px;">
    <span class="brand-dot" style="width:17px;height:17px;border-width:1px;"></span>
    <div><div class="brand-name" style="font-size:6px;">Dr Clara Whitfield</div><div class="brand-role" style="font-size:4px;">Obstetrician and Gynaecologist</div></div>
  </div>
  <div class="card-title" style="left:70px;top:50px;">Appointment</div>
  <div class="row hd" style="position:absolute;left:27px;top:72px;height:3px;"><span style="width:15px"></span><span style="width:5px"></span><span style="width:18px"></span><span style="width:25px"></span><span style="width:20px"></span><span style="width:20px"></span></div>
  <div class="row tx" style="position:absolute;left:27px;top:81px;height:2px;"><span style="width:80px"></span></div>
  <div class="rule" style="left:27px;top:93px;width:112px;"></div>
  <div class="rule" style="left:27px;top:106px;width:112px;"></div>
  <div class="row hd" style="position:absolute;left:27px;top:119px;height:3px;"><span style="width:15px"></span><span style="width:5px"></span><span style="width:18px"></span><span style="width:25px"></span><span style="width:20px"></span><span style="width:20px"></span></div>
  <div class="row tx" style="position:absolute;left:27px;top:128px;height:2px;"><span style="width:112px"></span></div>
  <div class="rule" style="left:27px;top:140px;width:112px;"></div>
  <div class="rule" style="left:27px;top:153px;width:112px;"></div>
  <div class="row hd" style="position:absolute;left:27px;top:165px;height:3px;"><span style="width:15px"></span><span style="width:5px"></span><span style="width:18px"></span><span style="width:25px"></span><span style="width:20px"></span><span style="width:20px"></span></div>
  <div class="row tx" style="position:absolute;left:27px;top:192px;height:2px;"><span style="width:70px"></span></div>
  <div class="mark" style="left:106px;top:222px;width:22px;height:22px;border-width:1px;"></div>
  <svg style="position:absolute;left:60px;top:252px;" width="80" height="14">
    <g fill="#73c19e"><rect width="14" height="2"/><rect y="5" width="24" height="2"/><rect x="40" y="10" width="18" height="2"/></g>
    <g fill="#a5a5a5"><rect x="16" width="60" height="2"/><rect x="26" y="5" width="54" height="2"/><rect x="8" y="10" width="30" height="2"/></g>
  </svg>
</section>
<section class="piece appt-front" style="left:269px;top:259px;width:233px;height:294px;">
  <div class="brand" style="position:absolute;left:26px;top:14px;gap:4px;">
    <span class="brand-dot" style="width:17px;height:17px;border-width:1px;"></span>
    <div><div class="brand-name" style="font-size:6px;">Dr Clara Whitfield</div><div class="brand-role" style="font-size:4px;">Obstetrician and Gynaecologist</div></div>
  </div>
  <div class="card-title" style="left:71px;top:49px;">Appointment Card</div>
  <div class="row hd" style="position:absolute;left:27px;top:71px;height:3px;"><span style="width:15px"></span><span style="width:5px"></span><span style="width:18px"></span><span style="width:25px"></span><span style="width:20px"></span><span style="width:20px"></span></div>
  <div class="row tx" style="position:absolute;left:27px;top:80px;height:2px;"><span style="width:85px"></span></div>
  <div class="rule" style="left:27px;top:93px;width:174px;"></div>
  <div class="rule" style="left:27px;top:106px;width:174px;"></div>
  <div class="row hd" style="position:absolute;left:27px;top:118px;height:3px;"><span style="width:15px"></span><span style="width:5px"></span><span style="width:18px"></span><span style="width:25px"></span><span style="width:20px"></span><span style="width:20px"></span></div>
  <div class="row tx" style="position:absolute;left:27px;top:127px;height:2px;"><span style="width:165px"></span></div>
  <div class="rule" style="left:27px;top:136px;width:174px;"></div>
  <div class="rule" style="left:27px;top:150px;width:176px;"></div>
  <div class="row hd" style="position:absolute;left:27px;top:163px;height:3px;"><span style="width:15px"></span><span style="width:5px"></span><span style="width:18px"></span><span style="width:25px"></span><span style="width:20px"></span><span style="width:20px"></span></div>
  <div class="row tx" style="position:absolute;left:27px;top:190px;height:2px;"><span style="width:70px"></span></div>
  <div class="mark" style="left:104px;top:220px;width:22px;height:22px;border-width:1px;"></div>
  <svg style="position:absolute;left:60px;top:251px;" width="120" height="14">
    <g fill="#73c19e"><rect width="14" height="2"/><rect y="5" width="24" height="2"/><rect x="40" y="10" width="18" height="2"/><rect x="58" y="5" width="30" height="2"/></g>
    <g fill="#a5a5a5"><rect x="16" width="90" height="2"/><rect x="26" y="5" width="30" height="2"/><rect x="90" y="5" width="22" height="2"/><rect x="8" y="10" width="30" height="2"/><rect x="60" y="10" width="45" height="2"/></g>
  </svg>
</section>

<!-- Envelope back and compliments slip -->
<section class="piece envelope" style="left:182px;top:718px;width:309px;height:155px;">
  <svg class="flap" width="309" height="37"><polygon points="0,0 309,0 298,37 11,37" fill="#1a958f"/></svg>
  <div class="mark" style="left:12px;top:98px;width:38px;height:38px;"></div>
</section>
<section class="piece comp-slip" style="left:249px;top:794px;width:310px;height:155px;">
  <div class="row hd" style="position:absolute;left:27px;top:108px;height:3px;"><span style="width:18px"></span><span style="width:5px"></span><span style="width:14px"></span><span style="width:5px"></span><span style="width:22px"></span><span style="width:12px"></span><span style="width:30px"></span><span style="width:32px"></span></div>
  <svg style="position:absolute;left:27px;top:117px;" width="170" height="30">
    <g fill="#a5a5a5"><rect width="165" height="2"/><rect y="5" width="160" height="2"/><rect y="10" width="165" height="2"/><rect y="15" width="160" height="2"/><rect y="20" width="68" height="2"/></g>
  </svg>
  <div class="mark" style="left:247px;top:102px;width:38px;height:38px;"></div>
</section>

<!-- Business cards -->
<div class="sheet-teal" style="left:705px;top:783px;width:176px;height:97px;"></div>
<section class="piece card-back" style="left:801px;top:807px;width:176px;height:97px;">
  <div class="back-text" style="left:79px;top:15px;font-size:9px;">Lorem ipsum<br>dolor consectetur</div>
  <div class="back-text" style="left:79px;top:41px;font-size:6px;color:#999;">dolor sit amet</div>
  <svg style="position:absolute;left:66px;top:66px;" width="100" height="20">
    <g fill="#a5a5a5"><rect x="30" width="40" height="2"/><rect y="6" width="42" height="2"/><rect x="72" y="6" width="26" height="2"/><rect x="20" y="12" width="40" height="2"/></g>
    <g fill="#73c19e"><rect x="12" width="16" height="2"/><rect x="44" y="6" width="26" height="2"/><rect y="12" width="18" height="2"/></g>
  </svg>
</section>
<section class="piece card-front" style="left:683px;top:791px;width:176px;height:97px;">
  <div class="brand" style="position:absolute;left:20px;top:36px;gap:6px;">
    <span class="brand-dot" style="width:34px;height:34px;"></span>
    <div><div class="brand-name" style="font-size:10px;">Dr Clara Whitfield</div><div class="brand-role" style="font-size:6px;">Obstetrician and Gynaecologist</div></div>
  </div>
</section>

</body>
</html>
```